Design a label for a dog shampoo names furbloom, the sell point of this series of shampoo is “just like wash your dogs with milk, not harm for your hand ”, the style could be gentle or professional or even amazing.

Use only 2 colors in the design job, the color of our logo could be changed, it depends on your whole page. Please design in CDR or ai.

update:
Pls do more change with the fonts when you design the front page, including title and details. Try more styles of fonts. Addition, this design will be printed on the bottle, no a label stick on it.
Updates

Do not put a real dog or animal on the page, Pay more attention to the types of fonts

Reason: Expect for more design idea.

Target Market(s)

people 20-30 years old who have dogs and cats at home

Industry/Entity Type

It Professional

Requirements
Nice to have
• It would be nice if you add some detail words in the design of the right side.

```html
<!DOCTYPE html>
<html lang="en">
<head>
<meta charset="utf-8">
<title>furbloom Super-Conditioning &amp; Nutrient Shampoo – Label</title>
<link rel="stylesheet" href="https://fonts.googleapis.com/css2?family=Arimo:ital,wght@0,400;0,700;1,400&family=Oswald:wght@500;600&family=Antic+Didone&family=Great+Vibes&display=swap">
<style>
  :root {
    --teal: #1fa9c9;
    --grey: #555a5e;
    --text: #3a3d40;
    --paper: #ffffff;
    --backdrop: #dcebf5;
    --caption: #5f6468;
  }
  * { box-sizing: border-box; margin: 0; padding: 0; }
  html, body { width: 1200px; height: 900px; overflow: hidden; }
  body {
    position: relative;
    background: var(--backdrop);
    font-family: "Arimo", Arial, sans-serif;
  }
  .caption {
    position: absolute;
    font-family: "Arimo", Arial, sans-serif;
    font-style: italic;
    font-size: 36px;
    color: var(--caption);
  }
  .caption--back { left: 362px; top: 186px; }
  .caption--front { left: 903px; top: 684px; }

  .label {
    position: absolute;
    background: var(--paper);
    border-radius: 20px;
    box-shadow: 0 2px 10px rgba(0,0,0,0.18);
  }
  .label--back { left: 342px; top: 243px; width: 314px; height: 600px; padding: 0 20px; }
  .label--front { left: 688px; top: 70px; width: 313px; height: 600px; }

  .brand {
    display: flex;
    align-items: center;
    justify-content: center;
    gap: 6px;
    height: 92px;
    font-family: "Arimo", Arial, sans-serif;
    font-weight: 700;
    font-size: 22px;
    color: var(--teal);
  }
  .brand__dot { width: 12px; height: 12px; border-radius: 50%; background: var(--teal); }

  .back-copy {
    font-size: 11px;
    line-height: 1.2;
    color: var(--text);
    text-align: justify;
  }
  .back-copy strong { color: var(--teal); }
  .back-copy h2 {
    font-size: 11.2px;
    font-weight: 700;
    color: var(--teal);
    margin: 10px 0 2px;
  }
  .directions { list-style: none; padding-left: 18px; text-align: left; }
  .directions li { position: relative; padding-left: 13px; }
  .directions li::before {
    content: "";
    position: absolute;
    left: 0; top: 3px;
    width: 5px; height: 5px;
    border: 2px solid var(--teal);
    border-radius: 50%;
  }
  .label--front svg { display: block; }
</style>
</head>
<body>
  <span class="caption caption--back">back</span>
  <span class="caption caption--front">front</span>

  <section class="label label--back">
    <div class="brand"><span class="brand__dot"></span>furbloom</div>
    <div class="back-copy">
      <p><strong>FURBLOOM Super-Conditioning &amp; Nutrient Shampoo</strong> is a specially formulated shampoo, rich in conditioners picked up from milk which subdivide and balance nutrition of pet's coat. More easier and better assimilate for coat from base to the end after using. With the help of minus-ion, the balancer of nutrition, rinses out quickly and completely to leave a soft, sparkling, and smooth coat. Safe and gentle enough to be used every day. Safe for even the most sensitive skin and coat, puppies, lactating bitches and cats.</p>
      <h2>DIRECTIONS:</h2>
      <ul class="directions">
        <li>Before shampooing, blush out pet's coat.</li>
        <li>Saturate dog's coat with lukewarm water.</li>
        <li>Dispense a small amount of shampoo into the palm of your hand.</li>
        <li>To clean coat, start at dog's head and work back towards the tail. Avoid getting shampoo into the dog's eyes and ears.</li>
        <li>Rinse coat sereral times with lukewarm water.</li>
        <li>Towel dry and gently comb or brush coat.</li>
      </ul>
      <h2>ACTIVE INGREDIENTS:</h2>
      <p>Hypochlorous Acid, Sodium Hypochlorite</p>
      <h2>USE PRECAUTIONS:</h2>
      <p>Harmful if swallowed. Do not inhale. Discontinue use if irritation develops and contact your veterinarian. For animal use only. Not for human use. Keep out of reach of children. Do not decant into smaller containers. Not for injection. Always consult with a Veterinarian for systemic conditions.</p>
      <h2>STORAGE AND DISPOSAL</h2>
      <p>Keep out of the tough of children. Replace Cap. Wrap in several layers of newspaper and discard in trash.</p>
    </div>
  </section>

  <section class="label label--front">
    <svg width="313" height="600" viewBox="0 0 313 600" aria-label="Front label">
      <circle cx="104" cy="57" r="6" fill="var(--teal)"/>
      <text x="164" y="65" text-anchor="middle" font-family="Arimo, Arial, sans-serif" font-weight="700" font-size="22" fill="var(--teal)">furbloom</text>

      <g font-family="Oswald, 'Arial Narrow', sans-serif" font-weight="600" fill="var(--grey)" text-anchor="middle">
        <text x="157" y="123" font-size="18.5">SUPER-CONDITIONING</text>
        <text x="157" y="179" font-size="18.5">NUTIENT SHAMPOO</text>
      </g>
      <text x="157" y="151" text-anchor="middle" font-family="'Great Vibes', cursive" font-size="22" fill="var(--teal)">&amp;</text>
      <text x="157" y="250" text-anchor="middle" font-family="'Antic Didone', serif" font-size="50" fill="var(--teal)" transform="translate(157 0) scale(0.85 1) translate(-157 0)">MILK</text>

      <path d="M112 392 H232 V467 H297 V573 Q297 585 285 585 H30 Q18 585 18 573 V467 H112 Z" fill="var(--grey)" role="img" aria-label="Grey silhouette of a dog sitting in a bathtub"/>

      <g fill="var(--teal)">
        <circle cx="45" cy="222" r="6"/><circle cx="26" cy="283" r="3.5"/>
        <circle cx="78" cy="303" r="7"/><circle cx="40" cy="317" r="3"/>
        <circle cx="197" cy="302" r="5"/><circle cx="251" cy="271" r="9"/>
        <circle cx="239" cy="225" r="4"/><circle cx="274" cy="198" r="4"/>
        <circle cx="62" cy="427" r="12"/><circle cx="97" cy="448" r="6"/>
        <circle cx="186" cy="370" r="7"/><circle cx="250" cy="384" r="4"/>
        <circle cx="247" cy="419" r="10"/><circle cx="273" cy="446" r="4"/>
        <circle cx="87" cy="399" r="4"/><circle cx="34" cy="449" r="4"/>
        <circle cx="97" cy="354" r="3"/><circle cx="131" cy="353" r="3"/>
        <circle cx="290" cy="318" r="3"/>

        <circle cx="146" cy="318" r="25"/>
        <circle cx="52" cy="366" r="25"/>
        <circle cx="261" cy="366" r="32"/>
      </g>
      <g font-family="Oswald, 'Arial Narrow', sans-serif" font-weight="600" fill="var(--paper)" text-anchor="middle">
        <text x="146" y="324" font-size="15" textLength="42" lengthAdjust="spacingAndGlyphs">SMOOTH</text>
        <text x="52" y="372" font-size="17" textLength="38" lengthAdjust="spacingAndGlyphs">SILKY</text>
        <text x="261" y="362" font-size="14" textLength="52" lengthAdjust="spacingAndGlyphs">MOISTURE</text>
        <text x="261" y="382" font-size="17" textLength="34" lengthAdjust="spacingAndGlyphs">RICH</text>
      </g>

      <text x="160" y="554" text-anchor="middle" font-family="Oswald, 'Arial Narrow', sans-serif" font-weight="600" font-size="16" fill="var(--paper)">1000 ML</text>
    </svg>
  </section>
</body>
</html>
```